Motor Insurance Quotation - New Quote format / New Template

We are a 40 year old insurance company called 'Velmor Insurance Agency L.L.C' in Dubai, UAE (Our logo / color design can and details can be found on www.velmorgulf-example.com).

Velmor provides all kinds of insurance solutions for its clients...currently is this modern fast paced world of ever changing technology and increasing competition we need to be ahead of our competitors...

In order to do so, we are in need to re-design our motor insurance quotation format / template and require it to be more attractive, modern and professional.
Since it is a text heavy format, we need it to look aesthetically appealing to our clients.

We would like to see designs that use our color code (as our website / sample quote currently used is attached)..these designs are required in pdf illustrator formats....i have also attached quotation formats used in the existing market. the template and the samples are only for reference and the templates are not to be followed.

Target Market(s)

UAE

Industry/Entity Type

Insurance

Font styles to use
Other font styles liked:
• arial

Requirements
Must have
• Aesthetic Design, Insurance details and covers provided in our quote, Velmor logo, color code (details can be found on our website)
Nice to have
• 1 page (short quote) and 2 page (detailed quote) designs to shared...

```html
<!DOCTYPE html>
<html lang="en">
<head>
<meta charset="UTF-8">
<title>Velmor – Motor Insurance Quotation</title>
<link href="https://fonts.googleapis.com/css2?family=Fira+Sans:wght@400;500;600;700&display=swap" rel="stylesheet">
<style>
  :root {
    --brand-navy: #27307c;
    --brand-purple: #6c2a7f;
    --pill-purple: #6e2a82;
    --ink: #2f2f2f;
    --value-ink: #3a3a3a;
    --muted: #6b6b6b;
    --rule: #d6d6d6;
    --page-bg: #ffffff;
    --canvas-bg: #ffffff;
  }
  * { box-sizing: border-box; margin: 0; padding: 0; }
  html, body {
    width: 848px; height: 1200px; overflow: hidden;
    background: var(--canvas-bg);
    font-family: "Fira Sans", Arial, sans-serif;
    color: var(--ink);
  }
  .quote-page {
    position: absolute; left: 29px; top: 30px;
    width: 789px; height: 1136px;
    background: var(--page-bg);
    box-shadow: 0 0 6px rgba(0,0,0,0.35);
  }
  .brand-name {
    position: absolute; left: 0; right: 0; top: 20px;
    text-align: center;
    font-size: 62px; font-weight: 400; letter-spacing: 0;
    color: var(--brand-navy); line-height: 1;
  }
  .quote-title {
    position: absolute; left: 0; right: 0; top: 104px;
    text-align: center;
    font-size: 25px; font-weight: 700; line-height: 30px;
    color: var(--brand-purple);
  }
  .title-rule {
    position: absolute; left: 18px; right: 21px; top: 143px;
    border-top: 1px solid var(--rule);
  }
  .meta { position: absolute; top: 148px; color: var(--muted); }
  .meta-label { font-size: 19px; font-weight: 600; line-height: 25px; }
  .meta-value { font-size: 18.3px; font-weight: 400; line-height: 24px; }
  .meta--reference { left: 18px; }
  .meta--issue { right: 21px; top: 146px; text-align: right; }

  .section-pill {
    position: absolute; left: 37px; width: 199px; height: 38px;
    border-radius: 19px;
    background: var(--pill-purple); color: #fff;
    font-size: 19px; font-weight: 600;
    display: flex; align-items: center; justify-content: center;
  }
  .detail-list {
    position: absolute; left: 0;
    display: grid; grid-template-columns: 236px 1fr;
    line-height: 24px;
  }
  .detail-label {
    text-align: right; font-weight: 600; font-size: 19px;
    padding-right: 19px; color: var(--ink);
  }
  .detail-value {
    border-left: 1px solid var(--rule);
    padding-left: 24px; color: var(--value-ink);
    font-size: 18.5px; font-weight: 400;
  }
  .cover-type {
    position: absolute; left: 126px; top: 832px;
    font-size: 19.6px; font-weight: 600; color: var(--ink);
  }
</style>
</head>
<body>
  <main class="quote-page">
    <div class="brand-name">VELMOR</div>
    <h1 class="quote-title">MOTOR COMPREHENSIVE, FIRE, THEFT &amp; THIRD PARTY LIABILITY</h1>
    <div class="title-rule"></div>

    <div class="meta meta--reference">
      <div class="meta-label">Quote Reference</div>
      <div class="meta-value">MVA/2016/00603OM</div>
    </div>
    <div class="meta meta--issue">
      <div class="meta-label">Date of Issue</div>
      <div class="meta-value">12/01/2017</div>
    </div>

    <div class="section-pill" style="top:256px">Driver Details</div>
    <dl class="detail-list" style="top:320px">
      <dt class="detail-label">Insured Name</dt><dd class="detail-value">Lamia Sarhani</dd>
      <dt class="detail-label">Address</dt><dd class="detail-value">Dubau</dd>
      <dt class="detail-label">Email</dt><dd class="detail-value">L.Sarhani@mailbox-example.com</dd>
      <dt class="detail-label">Phone Number</dt><dd class="detail-value">056 - 7390215</dd>
      <dt class="detail-label">Age</dt><dd class="detail-value">26 Years</dd>
    </dl>

    <div class="section-pill" style="top:512px">Vehicle Details</div>
    <dl class="detail-list" style="top:577px">
      <dt class="detail-label">Make</dt><dd class="detail-value">Arvenne</dd>
      <dt class="detail-label">Model</dt><dd class="detail-value">A16 I</dd>
      <dt class="detail-label">Year of Make</dt><dd class="detail-value">2011</dd>
      <dt class="detail-label">Seating Capacity</dt><dd class="detail-value">5</dd>
      <dt class="detail-label">Body</dt><dd class="detail-value">Saloon</dd>
    </dl>

    <div class="section-pill" style="top:769px">Type of Cover</div>
    <p class="cover-type">Comprehensive, Fire, Theft &amp; Third Party Liability</p>

    <div class="section-pill" style="top:925px">Quote Details</div>
    <dl class="detail-list" style="top:990px">
      <dt class="detail-label">Sum Insured</dt><dd class="detail-value">AED 40,000.00</dd>
      <dt class="detail-label">Premium</dt><dd class="detail-value">AED 1,740.00</dd>
      <dt class="detail-label">Excess</dt><dd class="detail-value">AED 350.00</dd>
    </dl>
  </main>
</body>
</html>
```